Oven Cleaning Business owner needs business card design

Hi there,
Would like for a business card to be designed for myself, the owner of a professional oven cleaning business on the Sunshine Coast.
Would like it to look sleek, and modern-ish. Bit creative is encouraged too.
Include following:
Name/title: Corin ter Haghe, Owner
Phone number: 1300 482 916
Email: info@hearthshinecrew.com.au
Website: www.hearthshinecrew.com.au

```html
<!DOCTYPE html>
<html lang="en">
<head>
<meta charset="utf-8">
<title>Corin ter Haghe – Business Card</title>
<link href="https://fonts.googleapis.com/css2?family=Arimo:wght@400;700&display=swap" rel="stylesheet">
<style>
  :root {
    --paper: #ffffff;
    --ink: #1f1f1f;
    --accent: #1fe0e0;
    --shape-light: #f2f2f2;
    --shape-dark: #000000;
    --rail: #efefef;
  }
  html, body {
    margin: 0;
    padding: 0;
    overflow: hidden;
    background: var(--paper);
  }
  .card {
    position: relative;
    width: 1200px;
    height: 720px;
    background: var(--paper);
    overflow: hidden;
    font-family: "Arimo", Arial, sans-serif;
    color: var(--ink);
  }
  .backdrop {
    position: absolute;
    inset: 0;
  }
  .brand-name {
    position: absolute;
    top: 36px;
    right: 30px;
    margin: 0;
    font-size: 34px;
    font-weight: 700;
    letter-spacing: 1px;
    text-transform: uppercase;
    color: var(--ink);
  }
  .rail {
    position: absolute;
    left: 158px;
    top: 139px;
    width: 50px;
    height: 450px;
    background: linear-gradient(to bottom, var(--rail) 0%, var(--rail) 88%, rgba(239,239,239,0) 100%);
  }
  .icon {
    position: absolute;
    left: 158px;
    width: 50px;
    height: 53px;
  }
  .icon-person { top: 160px; height: 62px; }
  .icon-phone { top: 335px; }
  .icon-mail { top: 419px; }
  .icon-web { top: 506px; }
  .identity {
    position: absolute;
    left: 245px;
    top: 140px;
    margin: 0;
    font-weight: 400;
  }
  .identity .name {
    display: block;
    font-size: 50px;
    font-weight: 400;
    letter-spacing: 0.5px;
    line-height: 1.1;
  }
  .identity .role {
    display: block;
    margin-top: 1px;
    font-size: 23px;
    font-weight: 400;
    line-height: 1.2;
  }
  .contact {
    position: absolute;
    left: 247px;
    margin: 0;
    font-size: 25px;
    line-height: 1;
  }
  .contact-phone { top: 350px; font-size: 25px; font-weight: 700; letter-spacing: 0.3px; }
  .contact-mail { top: 435px; }
  .contact-web { top: 520px; }
</style>
</head>
<body>
<div class="card">
  <svg class="backdrop" width="1200" height="720" viewBox="0 0 1200 720" aria-hidden="true">
    <circle cx="1090" cy="170" r="370" fill="var(--shape-light)"/>
    <circle cx="816" cy="720" r="180" fill="var(--shape-dark)"/>
  </svg>

  <p class="brand-name">Hearthshine Crew</p>

  <div class="rail"></div>

  <svg class="icon icon-person" viewBox="0 0 50 62" aria-hidden="true">
    <circle cx="25" cy="14" r="14" fill="var(--accent)"/>
    <path d="M0 42 Q0 30 12 30 L38 30 Q50 30 50 42 L50 54 Q50 60 44 60 L6 60 Q0 60 0 54 Z" fill="var(--accent)"/>
  </svg>

  <h1 class="identity">
    <span class="name">Corin ter Haghe</span>
    <span class="role">Owner</span>
  </h1>

  <svg class="icon icon-phone" viewBox="0 0 50 53" aria-hidden="true">
    <rect width="50" height="53" rx="8" fill="var(--accent)"/>
    <path fill="#fff" d="M15 13 Q12 15 12 19 Q13 30 22 38 Q30 44 35 42 Q38 41 39 38 L34 33 Q32 32 30 33 L28 35 Q23 32 19 26 L21 24 Q22 22 21 20 Z"/>
  </svg>
  <p class="contact contact-phone">1300 482 916</p>

  <svg class="icon icon-mail" viewBox="0 0 50 53" aria-hidden="true">
    <rect width="50" height="53" rx="8" fill="var(--accent)"/>
    <rect x="12" y="17" width="26" height="19" fill="none" stroke="#fff" stroke-width="2"/>
    <path d="M12 17 L25 28 L38 17 M12 36 L21 26 M38 36 L29 26" fill="none" stroke="#fff" stroke-width="2"/>
  </svg>
  <p class="contact contact-mail">info@hearthshinecrew.com.au</p>

  <svg class="icon icon-web" viewBox="0 0 50 53" aria-hidden="true">
    <rect width="50" height="53" rx="8" fill="var(--accent)"/>
    <g fill="none" stroke="#fff" stroke-width="2">
      <circle cx="24" cy="25" r="15"/>
      <ellipse cx="24" cy="25" rx="7" ry="15"/>
      <path d="M9 25 H39 M11 17 H37 M11 33 H37 M24 10 V40"/>
    </g>
    <path d="M33 32 L33 45 L36 42 L39 47 L41 46 L38 41 L42 41 Z" fill="#fff" stroke="var(--accent)" stroke-width="1"/>
  </svg>
  <p class="contact contact-web">www.hearthshinecrew.com.au</p>
</div>
</body>
</html>
```